Tarvel Business Card Design

We need a business card design for a new company in NJ called Tarvel LLC. We provide plumbing, sewer & drain cleaning, and full bath remodeling services. We need a logo design that will be used for several applications such as; cards, stickers, t shirts, and truck lettering. The company hopes to one day be a full service operation offering plumbing, heating, cooling, electric, so we need a design that is very general (aka no pipe wrenches). Colors will be royal blue,neon lime green, and would like to add diamond plate or steel plate to give it a very masculine feel and look.

Contact Information for Business Card

Tarvel LLC. ,Plumbing, Sewer & Drain Cleaning, Bath Remodeling
North Brunswick, NJ 08902
732.555.0148
Tarvelpipeworks.example
Info@tarvelpipeworks.example
Stay calm, ring tarvel!, Rick Movren- President
NJ Master Plumbing License: 58217, Residential & Commercial Service

Requirements
Should not have
• Tool icons
Script font

```html
<!DOCTYPE html>
<html lang="en">
<head>
<meta charset="utf-8">
<title>Tarvel LLC – Business Card</title>
<link href="https://fonts.googleapis.com/css2?family=Exo+2:ital,wght@0,400;0,600;0,700;0,800;1,700&display=swap" rel="stylesheet">
<style>
  :root {
    --navy: #1b2d5a;
    --icon-navy: #12305e;
    --lime: #76bf43;
    --ink: #231f20;
    --paper: #ffffff;
  }
  html, body {
    margin: 0;
    padding: 0;
    overflow: hidden;
    background: var(--paper);
  }
  .card {
    position: relative;
    width: 1200px;
    height: 702px;
    background: var(--paper);
    font-family: "Exo 2", Arial, sans-serif;
    color: var(--ink);
    overflow: hidden;
  }
  .brand {
    position: absolute;
    right: 110px;
    top: 84px;
    display: flex;
    align-items: center;
    gap: 24px;
  }
  .brand-dot {
    width: 72px;
    height: 72px;
    border-radius: 50%;
    background: var(--lime);
  }
  .brand-name {
    font-size: 110px;
    font-weight: 800;
    line-height: 1;
    color: var(--navy);
    letter-spacing: 1px;
  }
  .person {
    position: absolute;
    right: 113px;
    top: 232px;
    text-align: right;
  }
  .person-name {
    margin: 0;
    font-size: 51px;
    font-weight: 700;
    line-height: 1.1;
    color: var(--navy);
  }
  .person-title {
    margin: 0;
    font-size: 37px;
    font-weight: 400;
    line-height: 1.2;
    color: var(--ink);
  }
  .contact-list {
    list-style: none;
    margin: 0;
    padding: 0;
  }
  .contact-item {
    position: absolute;
    left: 89px;
    display: flex;
    align-items: center;
    font-size: 40px;
    font-weight: 400;
  }
  .contact-item svg { flex: none; fill: var(--icon-navy); }
  .contact-phone { top: 360px; }
  .contact-phone .contact-text { margin-left: 36px; }
  .contact-email { top: 446px; }
  .contact-email .contact-text { margin-left: 36px; }
  .contact-web { top: 506px; }
  .contact-web .contact-text { margin-left: 22px; }
  .license-band {
    position: absolute;
    left: 0;
    top: 589px;
    width: 1200px;
    height: 95px;
  }
  .license-text {
    position: absolute;
    left: 87px;
    top: 602px;
    margin: 0;
    font-size: 36px;
    font-weight: 700;
    font-style: italic;
    letter-spacing: 0.4px;
    color: var(--paper);
    line-height: 1.5;
  }
</style>
</head>
<body>
<main class="card">
  <div class="brand">
    <span class="brand-dot"></span>
    <span class="brand-name">Tarvel</span>
  </div>

  <div class="person">
    <h1 class="person-name">Rick Movren</h1>
    <p class="person-title">president</p>
  </div>

  <ul class="contact-list">
    <li class="contact-item contact-phone">
      <svg width="56" height="58" viewBox="0 0 56 58" aria-hidden="true">
        <path d="M12 4 L22 16 Q24 20 20 23 L16 27 Q20 37 29 43 L33 39 Q36 36 40 38 L51 47 Q53 50 50 53 L45 57 Q36 60 22 49 Q6 35 3 20 Q2 12 8 6 Z"/>
        <path d="M28 8 A22 22 0 0 1 49 29" fill="none" stroke="var(--icon-navy)" stroke-width="5" stroke-linecap="round"/>
        <path d="M28 18 A12 12 0 0 1 40 30" fill="none" stroke="var(--icon-navy)" stroke-width="5" stroke-linecap="round"/>
      </svg>
      <span class="contact-text">732.555.0148</span>
    </li>
    <li class="contact-item contact-email">
      <svg width="56" height="42" viewBox="0 0 56 42" aria-hidden="true">
        <rect x="3" y="3" width="50" height="36" rx="3" fill="none" stroke="var(--icon-navy)" stroke-width="6"/>
        <path d="M5 6 L28 24 L51 6 M5 36 L21 20 M51 36 L35 20" fill="none" stroke="var(--icon-navy)" stroke-width="5"/>
      </svg>
      <span class="contact-text">Info@tarvelpipeworks.example</span>
    </li>
    <li class="contact-item contact-web">
      <svg width="66" height="62" viewBox="0 0 66 62" aria-hidden="true">
        <g fill="none" stroke="var(--icon-navy)" stroke-width="4">
          <circle cx="28" cy="28" r="24"/>
          <ellipse cx="28" cy="28" rx="11" ry="24"/>
          <path d="M4 28 H52 M8 16 H48 M8 40 H40 M28 4 V52"/>
        </g>
        <path d="M38 30 L62 46 L52 48 L58 58 L53 61 L47 51 L40 57 Z" stroke="var(--paper)" stroke-width="2"/>
      </svg>
      <span class="contact-text">Tarvelpipeworks.example</span>
    </li>
  </ul>

  <svg class="license-band" viewBox="0 0 1200 95" aria-hidden="true">
    <polygon points="20,0 727,0 697,95 20,95" fill="var(--navy)"/>
    <polygon points="739,0 1183,0 1183,95 708,95" fill="var(--lime)"/>
  </svg>
  <p class="license-text">NJ Master Plumbing License: 58217</p>
</main>
</body>
</html>
```